TRAVEX CONSULTING / PROJECT MANAGEMENT WEB DESIGN

Design Brief: Travex Consulting Website

I own 'TRAVEX' business name and therefore can keep the name and logo simple i.e. TRAVEX only and incorporate consulting / Project Management within the design or text.

Purpose:

The purpose of this project is to create a website for Travex.com.au, a project management consulting company. The website will promote the company's services, allowing potential clients to learn more about Travex and its capabilities. The website should be professional, easy to navigate, and provide all necessary information for potential clients.

Target Audience:

Clients in the Oil & Gas, LNG, and Chemical industry
Businesses and organizations in need of project management and engineering consultancy services
Potential clients looking for information about the company and its services
Key Elements:
Clean and modern design that reflects the company's professional image and incorporates the company logo

Clear and easy-to-use navigation menu

“Homepage” that promotes the company's main services and includes the company's mission statement.

Services:

PROJECT MANAGEMENT
PROJECT ENGINEERING
QUALITY MANAGEMENT AND PROCESS DEVELOPMENT
BUSINESS CASE DEVELOPMENT
ENGINEERING & DESIGN MANAGEMENT
CONCEPT STUDIES AND PROJECT SUPPORT
CONSTRUCTION MANAGEMENT
CONTRACT MANAGEMENT / CLAIMS PROCUREMENT / SUPPLY CHAIN SUPPORT
COMMERCIAL LIABILITY & RISK MANAGEMENT

Mission Statement:

"Our mission at Travex is to provide expert project management and engineering consultancy services that help our clients achieve their goals and exceed their expectations. We will accomplish this by offering a full range of services, providing experienced and highly-qualified professionals, building strong relationships with our clients, continuously improving our services, and maintaining a reputation for excellence."

"About" page that includes client-supplied text about the company
"Contact" page with an editable form, email, and phone number for potential clients to get in touch with the company

Design Style:

Professional and modern
Clean and simple layout
Use of the company's colors and branding (subject to change)
Use of high-quality images that reflect the industry and services

Functionality:
Responsive design that is optimized for all devices and screen sizes

Website will be coded and uploaded to a content management system (CMS) for easy updates and maintenance
Website will be optimized for search engines and include all necessary SEO elements
Website will be fully tested for compatibility with all modern web browsers and devices
Website will be secured with an SSL certificate to ensure the safety of user data (client hosting includes SSL certificate).

Target Market(s)

Clients in the Oil & Gas, LNG, and Chemical industry Businesses and organizations in need of project management and engineering consultancy services Potential clients looking for information about the company and its services

Industry/Entity Type

Oil & Gas, LNG, and Chemical industry Businesses and organizations

Coding

Coded - Design and coding required

Number of Pages Required

3 page

Font styles to use
Sans Serif

Colors
0054AA
0677BA
7BADD7
CADEEF
E8F1F8
EB3D1F
EC4F4E
F09395
F8D3D4
FCEDEE
6B429C
8869AF
B7A5CE
E3DAEB
F3F0F8

Requirements
Must have
• HOME ABOUT AND CONTACT PAGE
Nice to have
• Fresh look, open to ideas
Should not have
• Stock images and hand shakes and meeting rooms..

```html
<!DOCTYPE html>
<html lang="en">
<head>
<meta charset="utf-8">
<title>Travex Resources – Project Management Consulting</title>
<link href="https://fonts.googleapis.com/css2?family=Ubuntu:wght@500;700&family=Roboto:wght@400;500;700&display=swap" rel="stylesheet">
<style>
:root{
  --blue:#2ba4f3;
  --blue-deep:#1e8fe0;
  --red:#e8412a;
  --ink:#1c1e22;
  --text:#3a3d42;
  --muted:#8d9199;
  --mist:#e7f4fd;
  --footer:#202328;
  --white:#ffffff;
}
*{box-sizing:border-box;margin:0;padding:0}
html,body{width:1200px;height:3510px;overflow:hidden}
body{position:relative;font-family:'Roboto',Arial,sans-serif;color:var(--text);background:var(--white)}
.abs{position:absolute}
.heading{font-family:'Ubuntu',Arial,sans-serif;font-weight:700;color:var(--ink)}
.rule{position:absolute;height:3px;width:34px;background:var(--blue)}
.btn-red{position:absolute;display:flex;align-items:center;justify-content:center;gap:8px;background:var(--red);color:#fff;font:700 13px 'Roboto',Arial,sans-serif;border-radius:22px;box-shadow:0 0 0 2px #fff,0 0 0 4px var(--red);letter-spacing:.2px}
.btn-red .dot{width:12px;height:12px;border-radius:50%;background:#fff;display:inline-flex;align-items:center;justify-content:center}
.btn-red .dot::after{content:"";border-left:4px solid var(--red);border-top:3px solid transparent;border-bottom:3px solid transparent;margin-left:1px}

/* header */
.site-header{position:absolute;left:0;top:0;width:1200px;height:100px;background:#fff;z-index:3}
.brand-box{position:absolute;left:144px;top:0;width:216px;height:129px;background:#fff;z-index:4;text-align:center}
.brand-box .mark{position:absolute;left:88px;top:22px;width:40px;height:40px;border-radius:50%;background:var(--blue)}
.brand-box .name{position:absolute;left:0;right:0;top:92px;font:700 17px 'Roboto',Arial,sans-serif;color:var(--blue)}
.nav a{position:absolute;top:40px;font:500 13px 'Roboto',Arial,sans-serif;color:var(--ink);text-decoration:none}
.nav .sep{position:absolute;top:39px;font-size:13px;color:var(--ink)}
.nav a.active{color:var(--red)}
.nav a.active::after{content:"";position:absolute;left:0;right:0;bottom:-10px;height:2px;background:var(--red)}
.btn-header{position:absolute;left:926px;top:28px;width:134px;height:40px;border-radius:22px;background:var(--blue);color:#fff;font:700 13px 'Roboto',Arial,sans-serif;display:flex;align-items:center;justify-content:center;box-shadow:0 0 0 2px #fff,0 0 0 4px var(--blue)}

/* hero */
.hero-photo{position:absolute;left:0;top:100px;width:1200px;height:700px;background:radial-gradient(ellipse at 58% 35%,#6b5a55 0%,#3f3d44 35%,#2a2c34 60%,#4e5258 100%)}
.hero-wave{position:absolute;left:0;top:600px;width:1200px;height:300px}
.hero-title{position:absolute;left:0;width:1172px;text-align:center;color:#fff;font-family:'Ubuntu',Arial,sans-serif;font-weight:700}
.social-rail span{position:absolute;left:1126px;width:12px;height:12px;border-radius:50%;background:#fff}
.scroll-label{position:absolute;left:1084px;top:492px;width:100px;transform:rotate(-90deg);color:#fff;font:500 10px 'Roboto',Arial,sans-serif;letter-spacing:1px;text-align:center}

/* services */
.services{position:absolute;left:0;top:820px;width:1200px;height:720px}
.svc-label{position:absolute;font:500 14px 'Roboto',Arial,sans-serif;color:var(--ink);line-height:23px}
.svc-label.r{text-align:right}

/* mission */
.mission-band{position:absolute;left:0;top:1588px;width:609px;height:490px;background:var(--mist)}
.mission-photo{position:absolute;left:609px;top:1588px;width:591px;height:490px;background:linear-gradient(120deg,#d8cfc2 0%,#b9b3ab 40%,#8f98a3 70%,#e9e6e0 100%)}
.mission-frame{position:absolute;left:591px;top:1807px;width:640px;height:288px;border:3px solid #ea6b5a;border-right:none;border-top:none;border-left-width:3px}
.mission-frame::before{content:"";position:absolute;left:-3px;top:-3px;width:20px;height:3px;background:#ea6b5a}
.body-copy{font-size:14px;line-height:22.4px;text-align:justify;color:var(--text)}

/* contact */
.contact-panel{position:absolute;left:133px;top:2660px;width:417px;height:358px;background:linear-gradient(135deg,#3aaaf5,#2296e6)}
.contact-panel .kicker{position:absolute;right:130px;top:96px;color:#fff;font:700 16px 'Roboto',Arial,sans-serif}
.contact-panel .big{position:absolute;right:130px;top:118px;text-align:right;color:#fff;font:700 36px/41px 'Ubuntu',Arial,sans-serif}
.contact-panel .bar{position:absolute;left:250px;top:262px;width:34px;height:3px;background:#fff}
.frame-blue{position:absolute;left:725px;top:2679px;width:339px;height:321px;border:4px solid var(--blue)}
.form-card{position:absolute;left:463px;top:2708px;width:583px;height:404px;background:#fff;box-shadow:0 8px 30px rgba(0,0,0,.12)}
.form-card h3{position:absolute;left:49px;top:38px;font:700 24px 'Ubuntu',Arial,sans-serif;color:var(--ink)}
.field{position:absolute;width:214px}
.field label{display:block;font:500 14px 'Roboto',Arial,sans-serif;color:var(--ink)}
.field .val{display:block;margin-top:14px;padding-bottom:9px;font-size:11.5px;color:var(--muted);border-bottom:1px solid #d4d7dc}
.send-btn{position:absolute;left:469px;top:303px;width:60px;height:60px;border-radius:50%;background:var(--red)}

/* footer */
.footer{position:absolute;left:0;top:2987px;width:1200px;height:468px;background:var(--footer)}
.footer h4{position:absolute;font:700 16px 'Roboto',Arial,sans-serif;color:#fff}
.footer .u{position:absolute;height:2px;width:58px;background:var(--blue)}
.footer .link{position:absolute;font-size:12px;color:#d5d7da}
.bottom-bar{position:absolute;left:0;top:3455px;width:1200px;height:55px;background:var(--red)}
.bottom-bar span{position:absolute;top:20px;font-size:12.5px;color:#fff}
</style>
</head>
<body>

<header class="site-header">
  <nav class="nav">
    <a class="active" style="left:405px">HOME</a>
    <span class="sep" style="left:483px">|</span>
    <a style="left:527px">ABOUT US</a>
    <span class="sep" style="left:634px">|</span>
    <a style="left:678px">SERVICES</a>
    <span class="sep" style="left:782px">|</span>
    <a style="left:826px">CONTACT</a>
  </nav>
  <div class="btn-header">GET STARTED</div>
</header>
<div class="brand-box"><span class="mark"></span><span class="name">TRAVEX RESOURCES</span></div>

<section class="hero">
  <div class="hero-photo" role="img" aria-label="Smiling consultant working on a laptop in a bright office"></div>
  <svg class="hero-wave" viewBox="0 600 1200 300" aria-hidden="true">
    <path d="M0 730 C60 772 140 794 260 792 C480 786 620 704 800 694 C960 686 1100 690 1200 676 L1200 900 L0 900 Z" fill="#fff"/>
    <path d="M190 797 C430 790 610 710 820 700 C1000 692 1130 745 1200 878 L1200 790 C1120 712 1000 686 820 690 C610 698 430 782 190 797 Z" fill="var(--blue)"/>
    <circle cx="600" cy="733" r="28" fill="#fff" stroke="var(--blue-deep)" stroke-width="2"/>
    <path d="M590 724 L600 733 L610 724 M590 732 L600 741 L610 732" fill="none" stroke="#2b4f8c" stroke-width="2.4" stroke-linecap="round"/>
  </svg>
  <div class="hero-title" style="top:436px;font-size:25px">WELCOME TO</div>
  <div class="hero-title" style="top:486px;font-size:54px;letter-spacing:-1px">TRAVEX RESOURCES</div>
  <div class="btn-red" style="left:514px;top:585px;width:146px;height:36px">GET STARTED <span class="dot"></span></div>
  <div class="social-rail">
    <span style="top:245px;width:22px;height:22px;left:1121px;background:none;border:1.5px solid #fff"></span>
    <span style="top:275px"></span>
    <span style="top:302px"></span>
    <span style="top:328px"></span>
  </div>
  <div class="abs" style="left:1132px;top:358px;width:1px;height:56px;background:#fff"></div>
  <div class="scroll-label">SCROLL DOWN</div>
  <svg class="abs" style="left:1122px;top:560px" width="20" height="30" viewBox="0 0 20 30" aria-hidden="true">
    <circle cx="10" cy="10" r="8" fill="var(--blue)"/>
    <path d="M10 6 V26 M4 20 L10 26 L16 20" fill="none" stroke="#fff" stroke-width="1.6"/>
  </svg>
</section>

<section class="services">
  <div class="heading abs" style="left:0;width:1210px;top:56px;text-align:center;font-size:31px">OUR SERVICES</div>
  <div class="rule" style="left:589px;top:95px"></div>
  <svg class="abs" style="left:0;top:0" width="1200" height="720" viewBox="0 0 1200 720" aria-hidden="true">
    <g fill="none" stroke="var(--blue)" stroke-width="1.6">
      <circle cx="604" cy="352" r="158" stroke-width="2.6"/>
      <path d="M454 172 H508 L537 211"/>
      <path d="M756 172 H701 L671 211"/>
      <path d="M368 276 H419 L448 316"/>
      <path d="M840 276 H804 L759 316"/>
      <path d="M368 418 H419 L447 380"/>
      <path d="M844 418 H790 L763 380"/>
      <path d="M458 537 H508 L539 498"/>
      <path d="M752 537 H699 L670 498"/>
      <path d="M601 512 V558"/>
    </g>
    <g fill="#fff" stroke="var(--red)" stroke-width="2">
      <circle cx="537" cy="211" r="7"/><circle cx="671" cy="211" r="7"/>
      <circle cx="448" cy="316" r="7"/><circle cx="759" cy="316" r="7"/>
      <circle cx="447" cy="380" r="7"/><circle cx="763" cy="380" r="7"/>
      <circle cx="539" cy="498" r="7"/><circle cx="670" cy="498" r="7"/>
      <circle cx="601" cy="512" r="7"/>
    </g>
    <g fill="var(--red)">
      <circle cx="454" cy="172" r="4.5"/><circle cx="756" cy="172" r="4.5"/>
      <circle cx="368" cy="276" r="4.5"/><circle cx="840" cy="276" r="4.5"/>
      <circle cx="368" cy="418" r="4.5"/><circle cx="844" cy="418" r="4.5"/>
      <circle cx="458" cy="537" r="4.5"/><circle cx="752" cy="537" r="4.5"/>
      <circle cx="601" cy="558" r="4.5"/>
    </g>
    <g fill="#fff" stroke="var(--blue)" stroke-width="2">
      <circle cx="403" cy="166" r="30"/><circle cx="806" cy="166" r="30"/>
      <circle cx="313" cy="272" r="30"/><circle cx="893" cy="272" r="30"/>
      <circle cx="312" cy="422" r="30"/><circle cx="896" cy="422" r="30"/>
      <circle cx="405" cy="542" r="30"/><circle cx="805" cy="542" r="30"/>
      <circle cx="603" cy="612" r="30"/>
    </g>
    <g fill="none" stroke="var(--red)" stroke-width="1.6" stroke-linecap="round" stroke-linejoin="round">
      <circle cx="403" cy="166" r="9"/><circle cx="403" cy="166" r="3"/>
      <rect x="798" y="156" width="16" height="20" rx="2"/><path d="M802 163 H810 M802 169 H810"/>
      <rect x="303" y="262" width="20" height="16" rx="1"/><path d="M307 267 H319 M307 272 H315"/>
      <path d="M883 282 V268 L893 262 L903 268 V282 Z"/>
      <path d="M303 422 A9 9 0 1 1 321 422"/><path d="M321 422 L318 418 M321 422 L324 418"/>
      <rect x="886" y="413" width="20" height="15" rx="1"/><path d="M890 431 H902"/>
      <circle cx="405" cy="542" r="9"/><path d="M401 542 L404 545 L410 538"/>
      <rect x="796" y="533" width="18" height="18" rx="2"/><path d="M800 539 H810 M800 544 H807"/>
      <circle cx="603" cy="612" r="9"/><circle cx="603" cy="612" r="4"/>
    </g>
    <circle cx="604" cy="330" r="22" fill="var(--blue)"/>
  </svg>
  <div class="abs" style="left:470px;width:270px;top:393px;text-align:center;font:700 23px 'Roboto',Arial,sans-serif;color:var(--blue)">TRAVEX RESOURCES</div>

  <div class="svc-label r" style="right:842px;top:154px">Project Management</div>
  <div class="svc-label" style="left:857px;top:143px">Project Engineering</div>
  <div class="svc-label r" style="right:930px;top:261px">Business Case Development</div>
  <div class="svc-label" style="left:940px;top:260px">Construction Management</div>
  <div class="svc-label r" style="right:932px;top:410px">Concept Studies And<br>Project Support</div>
  <div class="svc-label" style="left:941px;top:410px">Engineering &amp; Design<br>Management</div>
  <div class="svc-label r" style="right:840px;top:524px">Commercial Liability<br>&amp; Risk Management</div>
  <div class="svc-label" style="left:853px;top:530px">Contract Management</div>
  <div class="svc-label" style="left:0;width:1240px;text-align:center;top:652px">Quality Management And Process Development</div>
</section>

<section class="mission">
  <div class="mission-band"></div>
  <div class="mission-frame"></div>
  <div class="mission-photo" role="img" aria-label="Thoughtful professional reading notes beside a laptop"></div>
  <svg class="abs" style="left:578px;top:1560px" width="128" height="100" aria-hidden="true">
    <defs><pattern id="dotgrid" width="15.5" height="15.5" patternUnits="userSpaceOnUse"><circle cx="2" cy="2" r="1.6" fill="#3a3d55"/></pattern></defs>
    <rect x="0" y="0" width="128" height="18" fill="url(#dotgrid)"/>
    <rect x="0" y="0" width="34" height="100" fill="url(#dotgrid)"/>
  </svg>
  <div class="heading abs" style="left:142px;top:1673px;font-size:32px">OUR MISSION</div>
  <div class="rule" style="left:142px;top:1722px"></div>
  <p class="body-copy abs" style="left:142px;top:1741px;width:374px">Our mission at Travex is to provide expert project management and engineering consultancy services that help our clients achieve their goals and exceed their expectations. We will accomplish this by offering a full range of services, providing experienced and highly-qualified professionals, building strong relationships with our clients, continuously improving our services, and maintaining a reputation for excellence</p>
  <div class="btn-red" style="left:142px;top:1947px;width:148px;height:38px">LEARN MORE <span class="dot"></span></div>
</section>

<section class="about">
  <div class="abs" style="left:163px;top:2230px;width:360px;text-align:center;font:700 64px 'Roboto',Arial,sans-serif;color:var(--blue)">TRAVEX</div>
  <div class="heading abs" style="left:583px;top:2185px;font-size:32px">ABOUT US</div>
  <div class="rule" style="left:583px;top:2233px"></div>
  <p class="body-copy abs" style="left:583px;top:2251px;width:451px">Lorem ipsum dolor sit amet, consectetur adipiscing elit, sed do eiusmod tempor incididunt ut labore et dolore magna aliqua. Ut enim ad minim veniam, quis nostrud exercitation ullamco laboris nisi ut aliquip ex ea commodo consequat. Duis aute irure dolor in reprehenderit in voluptate velit esse cilluLorem ipsum dolor sit amet, consectetur adipiscing elit, sed do eiusmod tempor incididunt ut labore et dolore magna aliqua. Ut enim ad minim veniam, quis nostrud exercitation ullamco laboris nisi ut aliquip ex ea commodo consequat irure dolor in reprehenderit in voluptate velit esse cillum dolore eu fugiat nulla pariaturm liquip ex ea commodo consequat irure dolor i</p>
  <div class="btn-red" style="left:583px;top:2493px;width:148px;height:38px">LEARN MORE <span class="dot"></span></div>
</section>

<div class="footer"></div>

<section class="contact">
  <div class="contact-panel" role="img" aria-label="Blue-tinted photo of hands typing on a laptop">
    <div class="kicker">CONTACT US</div>
    <div class="big">Let’s Do<br>Good<br>Together!</div>
    <div class="bar"></div>
  </div>
  <svg class="abs" style="left:104px;top:2936px" width="112" height="112" aria-hidden="true">
    <defs><pattern id="dotgrid2" width="9" height="9" patternUnits="userSpaceOnUse"><circle cx="2" cy="2" r="1.4" fill="var(--blue)"/></pattern></defs>
    <rect x="0" y="0" width="28" height="112" fill="url(#dotgrid2)"/>
    <rect x="0" y="82" width="112" height="30" fill="url(#dotgrid2)"/>
  </svg>
  <div class="frame-blue"></div>
  <div class="form-card">
    <h3>Send Us A Message</h3>
    <div class="field" style="left:53px;top:101px"><label>Your Name</label><span class="val">Jane Doe</span></div>
    <div class="field" style="left:311px;top:101px"><label>Company</label><span class="val">Lorem ipsum dolor sit amet</span></div>
    <div class="field" style="left:53px;top:187px"><label>Email Address</label><span class="val">jane.doe@example.com</span></div>
    <div class="field" style="left:311px;top:187px"><label>Phone</label><span class="val">01122-555-010-789</span></div>
    <div class="field" style="left:53px;top:274px;width:412px"><label>Message</label><span class="val" style="padding-bottom:38px">Hi, do you have a moment to talk abo...|</span></div>
    <div class="send-btn">
      <svg width="60" height="60" viewBox="0 0 60 60" aria-hidden="true"><path d="M21 31 L39 22 L33 40 L30 33 Z" fill="#fff"/></svg>
    </div>
  </div>
</section>

<footer>
  <div class="abs" style="left:222px;top:3232px;width:40px;height:40px;border-radius:50%;background:var(--blue)"></div>
  <div class="abs" style="left:150px;top:3307px;font:700 18px 'Roboto',Arial,sans-serif;color:var(--blue)">TRAVEX RESOURCES</div>

  <div class="footer" style="background:none;top:0;height:0"></div>
  <h4 class="abs" style="left:376px;top:3186px;font:700 16px 'Roboto',Arial,sans-serif;color:#fff">QUICK LINKS</h4>
  <div class="abs" style="left:376px;top:3217px;width:58px;height:2px;background:var(--blue)"></div>
  <div class="abs" style="left:381px;top:3239px;font-size:12px;color:#d5d7da">Home</div>
  <div class="abs" style="left:381px;top:3269px;font-size:12px;color:#d5d7da">About Us</div>
  <div class="abs" style="left:381px;top:3300px;font-size:12px;color:#d5d7da">Services</div>
  <div class="abs" style="left:381px;top:3330px;font-size:12px;color:#d5d7da">Contact</div>

  <h4 class="abs" style="left:541px;top:3186px;font:700 16px 'Roboto',Arial,sans-serif;color:#fff">CONTACT US</h4>
  <div class="abs" style="left:541px;top:3217px;width:58px;height:2px;background:var(--blue)"></div>
  <svg class="abs" style="left:540px;top:3244px" width="20" height="145" viewBox="0 0 20 145" aria-hidden="true" fill="#fff">
    <path d="M5 5 L8 5 L9 8 L7.5 9.5 C8.5 11.5 9.5 12.5 11.5 13.5 L13 12 L16 13 L16 16 C10 16 5 11 5 5 Z"/>
    <path d="M3 41 H17 V51 H3 Z M3 41 L10 47 L17 41" stroke="#202328" stroke-width="1"/>
    <path d="M10 76 C6 76 4.5 79 4.5 81 C4.5 85 10 90 10 90 C10 90 15.5 85 15.5 81 C15.5 79 14 76 10 76 Z M10 79 A2 2 0 1 0 10.01 79 Z" fill-rule="evenodd"/>
    <rect x="4" y="128" width="12" height="11" rx="1"/><rect x="6" y="124" width="8" height="5" fill="none" stroke="#fff"/>
  </svg>
  <div class="abs" style="left:571px;top:3247px;font-size:12px;color:#d5d7da">+1 555-010-2040</div>
  <div class="abs" style="left:571px;top:3285px;font-size:12px;color:#d5d7da">info@travexresources.com</div>
  <div class="abs" style="left:571px;top:3314px;width:200px;font-size:12px;line-height:19px;color:#d5d7da">23.E Lorem ipsum dolor adipiscing elited sed do eiusmod tempored</div>
  <div class="abs" style="left:571px;top:3372px;font-size:12px;color:#d5d7da">555-010-7788</div>

  <h4 class="abs" style="left:808px;top:3186px;font:700 16px 'Roboto',Arial,sans-serif;color:#fff">SUBSCRIBE TO OUR BLOG</h4>
  <div class="abs" style="left:808px;top:3217px;width:58px;height:2px;background:var(--blue)"></div>
  <div class="abs" style="left:813px;top:3238px;width:230px;font-size:11.5px;line-height:19px;color:#d5d7da">Sign up today to get resources on how to attract and retain more customers!</div>
  <div class="abs" style="left:813px;top:3289px;width:234px;height:33px;border-radius:17px;background:#fff;overflow:hidden">
    <span class="abs" style="left:26px;top:10px;font-size:9.5px;color:var(--muted)">Email Address</span>
    <span class="abs" style="left:12px;top:13px;width:9px;height:7px;border:1px solid var(--muted)"></span>
    <span class="abs" style="left:190px;top:0;width:44px;height:33px;background:var(--blue)"></span>
    <svg class="abs" style="left:201px;top:6px" width="22" height="22" viewBox="0 0 22 22" aria-hidden="true"><path d="M4 11 L18 5 L14 18 L11 13 Z" fill="#fff"/></svg>
  </div>
  <div class="abs" style="left:810px;top:3343px;width:28px;height:28px;border-radius:50%;background:#fff"></div>
  <div class="abs" style="left:846px;top:3343px;width:28px;height:28px;border-radius:50%;background:var(--blue)"></div>
  <div class="abs" style="left:882px;top:3343px;width:28px;height:28px;border-radius:50%;background:#fff"></div>
  <div class="abs" style="left:919px;top:3343px;width:28px;height:28px;border-radius:50%;background:#fff"></div>

  <div class="bottom-bar">
    <span style="left:144px">Copyright© 2023 Travex Resources &nbsp;|&nbsp; All Rights Reserved</span>
    <span style="left:824px">Terms and Conditions &nbsp;&nbsp;|&nbsp;&nbsp; Privacy Policy</span>
  </div>
</footer>

</body>
</html>
```